CD Label Design Project

I need a CD label (circular) designed for a new company called DuctTradeRise.net. The CD is for an interview that has been done that will be mailed out to prospects who join the mailing list.
The CD itself is titled “Nine Quiet Errors Every Furnace Shop Keeps Repeating Daily.”

This title will need to be on the cd. The business itself is a marketing and coaching business for HVAC business owners so a design that communicates professionalism and business growth is essential. Ideally using colours from the logo in the design.
Updates

Just a quick note, the brief wasn't entirely clear. The design is for a CD label (circular) not a square cover. Thanks everyone.

Target Market(s)

HVAC (heating and cooling) business owners

Industry/Entity Type

Marketing

Requirements
Must have
• The title of the cd
Should not have
• images of heating or cooling systems
no images of money of cash

```html
<!DOCTYPE html>
<html lang="en">
<head>
<meta charset="utf-8">
<title>Nine Quiet Errors Every Furnace Shop Keeps Repeating Daily</title>
<link href="https://fonts.googleapis.com/css2?family=Bebas+Neue&display=swap" rel="stylesheet">
<style>
  :root {
    --page: #eceef1;
    --navy-deep: #141c28;
    --navy-mid: #24324a;
    --orange-hot: #ff6a00;
    --orange-deep: #e24e00;
    --white: #ffffff;
    --logo-ink: #1d2b44;
    --tile-edge: #d9dde3;
  }
  * { margin: 0; padding: 0; box-sizing: border-box; }
  html, body { width: 1200px; height: 1081px; overflow: hidden; background: var(--page); }
  .canvas {
    position: relative;
    width: 1200px;
    height: 1081px;
    overflow: hidden;
    font-family: "Bebas Neue", "Arial Narrow", sans-serif;
  }
  .disc {
    position: absolute; left: 70px; top: 10px;
    width: 1060px; height: 1060px;
    border-radius: 50%;
    overflow: hidden;
    box-shadow: 0 0 0 2px #d3d7dd;
  }
  .sky-band {
    position: absolute; left: 0; top: 0; width: 1060px; height: 250px;
    background:
      radial-gradient(ellipse 360px 220px at 50% 100%, rgba(80,100,130,0.45), transparent 70%),
      linear-gradient(180deg, var(--navy-deep) 0%, var(--navy-mid) 100%);
  }
  .title-band {
    position: absolute; left: 0; top: 250px; width: 1060px; height: 810px;
    background: linear-gradient(180deg, var(--orange-hot) 0%, #f55d00 50%, var(--orange-deep) 100%);
  }
  .glow-strip {
    position: absolute; left: 180px; top: 240px; width: 700px; height: 90px;
    background: radial-gradient(ellipse 50% 50% at 50% 40%, rgba(255,200,90,0.85), rgba(255,150,40,0.25) 65%, transparent 100%);
  }
  .brand-tile {
    position: absolute; left: 400px; top: 0; width: 260px; height: 140px;
    background: var(--white);
    border: 4px solid var(--tile-edge);
    border-top: none;
    display: flex; align-items: flex-end; justify-content: center;
    padding-bottom: 26px;
    box-shadow: 0 4px 14px rgba(0,0,0,0.35);
  }
  .brand-name { font-size: 38px; color: var(--logo-ink); letter-spacing: 1px; }
  .number-ball {
    position: absolute; left: 450px; top: 165px; width: 160px; height: 160px;
  }
  .title-lines {
    position: absolute; left: 0; width: 1060px;
    text-align: center; color: var(--white);
    font-weight: 400; font-size: 84px; line-height: 96px; letter-spacing: 1px;
    text-shadow: 0 3px 6px rgba(140,40,0,0.45);
  }
  .title-lines span { display: block; }
  .title-top { top: 330px; }
  .title-bottom { top: 640px; }
  .spindle-ring {
    position: absolute; left: 440px; top: 440px; width: 180px; height: 180px;
    border-radius: 50%;
    border: 2px solid rgba(255,255,255,0.35);
    background: rgba(255,255,255,0.08);
  }
  .spindle-hole {
    position: absolute; left: 480px; top: 480px; width: 100px; height: 100px;
    border-radius: 50%;
    background: var(--page);
    box-shadow: inset 0 2px 6px rgba(0,0,0,0.25);
  }
</style>
</head>
<body>
  <div class="canvas">
    <main class="disc">
      <div class="sky-band"></div>
      <div class="title-band"></div>
      <div class="glow-strip"></div>

      <header class="brand-tile">
        <span class="brand-name">DuctTradeRise.net</span>
      </header>

      <svg class="number-ball" viewBox="0 0 224 224" aria-hidden="true">
        <defs>
          <radialGradient id="ballFill" cx="42%" cy="30%" r="75%">
            <stop offset="0" stop-color="#ffd08a"/>
            <stop offset="0.35" stop-color="#ff8a1e"/>
            <stop offset="0.8" stop-color="#e85300"/>
            <stop offset="1" stop-color="#b83a00"/>
          </radialGradient>
          <radialGradient id="ballShine" cx="50%" cy="20%" r="50%">
            <stop offset="0" stop-color="#ffffff" stop-opacity="0.8"/>
            <stop offset="1" stop-color="#ffffff" stop-opacity="0"/>
          </radialGradient>
        </defs>
        <circle cx="112" cy="112" r="108" fill="url(#ballFill)"/>
        <ellipse cx="112" cy="58" rx="70" ry="42" fill="url(#ballShine)"/>
        <text x="114" y="170" text-anchor="middle" font-family="Bebas Neue, sans-serif" font-size="170" fill="#ffffff">9</text>
      </svg>

      <h1 class="title-lines title-top" aria-label="Nine Quiet Errors Every Furnace Shop Keeps Repeating Daily">
        <span>Quiet Errors</span>
      </h1>

      <div class="spindle-ring"></div>
      <div class="spindle-hole"></div>

      <p class="title-lines title-bottom" aria-hidden="true">
        <span>Every Furnace Shop</span>
        <span>Keeps Repeating</span>
        <span>Daily</span>
      </p>
    </main>
  </div>
</body>
</html>
```